依頼概要
■依頼の目的/概要
インフルエンザワクチンのポスターを作成して頂きたいです。
クリニック内の待合室に掲示します。

■依頼詳細
A2サイズです。
温かみのある柔らかいデザインをお願いします。
ポスターには、人のイラスト入りでお願いします。イラストはご自身で書いてくださってもいいですし、フリー素材でも構いません。
色合いは当院ホームページを参考にしてください。
当院ホームページ https://temuzeku.com/

記載する内容については、添付ファイルを参照してください。
ロゴデータは当選決定後に送らせて頂きます。

納品は、元データ(aiファイルやpsdファイル)とPNG書き出しでお願いします。

■重視する点
過去・現在までにデザインの経験のある方を希望致します。

その他何かご不明な点がございましたら、お気軽にご質問下さい。
よろしくお願いいたします。

文字が大きく読みやすい、温かみのあるデザインです。

皆さま、この度は当コンペにご参加いただき、誠にありがとうございます。
どれも力作で魅力的で選ぶのが大変でした。
今後ともどうぞよろしくお願いします。

```html
<!DOCTYPE html>
<html lang="ja">
<head>
<meta charset="utf-8">
<title>インフルエンザ予防接種 | 手武内科クリニック</title>
<link href="https://fonts.googleapis.com/css2?family=M+PLUS+Rounded+1c:wght@400;700;800&display=swap" rel="stylesheet">
<style>
:root{
  --green:#86b83c;
  --green-dark:#5f9128;
  --green-pale:#eef5dc;
  --orange:#f2a33a;
  --orange-dark:#e0882a;
  --orange-pale:#fdf0da;
  --cream:#fdf9ea;
  --ink:#4d4036;
  --white:#ffffff;
}
*{margin:0;padding:0;box-sizing:border-box}
html,body{width:849px;height:1200px;overflow:hidden;background:var(--white)}
body{font-family:"M PLUS Rounded 1c",sans-serif;color:var(--ink)}
.poster{position:relative;width:849px;height:1200px;background:var(--cream);border:14px solid var(--green);overflow:hidden}
.poster::after{content:"";position:absolute;inset:6px;border:2px solid var(--orange);border-radius:4px;pointer-events:none}
.headline{position:absolute;top:18px;left:0;right:0;text-align:center;font-size:33px;font-weight:800;color:var(--orange-dark);letter-spacing:.06em}
.headline-arc{position:absolute;top:62px;left:220px}
.family-art{position:absolute;top:95px;left:150px;width:660px;height:380px;border-radius:50% 50% 24px 24px/40% 40% 24px 24px;background:radial-gradient(ellipse at 50% 40%,#fbe3c6 0%,#f6d3a6 35%,#cfe3a8 75%,#eaf2d4 100%)}
.badge{position:absolute;top:335px;left:28px;width:150px;height:150px;border-radius:50%;background:var(--orange);color:var(--white);display:flex;flex-direction:column;align-items:center;justify-content:center;font-weight:800;box-shadow:0 0 0 5px var(--white)}
.badge .date{font-size:24px}
.badge .date small{font-size:13px}
.badge .note{font-size:28px;margin-top:2px}
.title-band{position:absolute;top:492px;left:150px;right:20px;height:72px;background:var(--green);color:var(--white);font-size:42px;font-weight:800;letter-spacing:.1em;display:flex;align-items:center;justify-content:center;border-radius:36px 0 0 36px}
.points{position:absolute;top:590px;left:60px;right:40px;list-style:none}
.points li{position:relative;padding-left:38px;font-size:22px;font-weight:700;line-height:1.6;margin-bottom:10px}
.points svg{position:absolute;left:0;top:6px}
.fee-label{position:absolute;top:800px;left:50px;font-size:20px;font-weight:800;color:var(--green-dark)}
.fee-label::before{content:"";display:inline-block;width:14px;height:14px;border-radius:50%;background:var(--green);margin-right:8px}
.fee-box{position:absolute;top:832px;height:210px;border-radius:14px;padding:16px 20px}
.fee-young{left:40px;width:365px;background:var(--green-pale);border:3px solid var(--green)}
.fee-senior{left:420px;width:375px;background:var(--orange-pale);border:3px solid var(--orange)}
.fee-who{font-size:24px;font-weight:800;margin-bottom:8px}
.fee-young .fee-who{color:var(--green-dark)}
.fee-senior .fee-who{color:var(--orange-dark)}
.fee-who small{font-size:12px;font-weight:400;color:var(--ink);margin-left:6px}
.price{font-size:34px;font-weight:800;line-height:1.25}
.price small{font-size:16px;font-weight:700}
.price.second{font-size:26px}
.period{font-size:19px;font-weight:700;margin-top:4px}
.period span{background:var(--orange);color:var(--white);border-radius:4px;padding:0 8px;margin-right:8px;font-size:16px}
.fine{font-size:11px;line-height:1.5;margin-top:8px}
.footer{position:absolute;left:0;right:0;bottom:0;height:125px;background:var(--white);display:flex;align-items:center;justify-content:space-between;padding:0 36px}
.clinic .dept{font-size:11px;margin-bottom:4px}
.clinic .name{display:flex;align-items:center;gap:10px;font-size:32px;font-weight:800;color:var(--green-dark)}
.clinic .mark{width:30px;height:30px;border-radius:50%;background:var(--green)}
.contact{display:flex;align-items:center;gap:14px;font-size:13px;font-weight:700;line-height:1.7;text-align:right}
.contact .url{font-weight:400;font-size:12px}
.contact .qr-space{width:68px;height:68px;border:2px solid var(--green-pale);border-radius:6px}
</style>
</head>
<body>
<div class="poster">
  <p class="headline">家族みんなで、今年も安心！</p>
  <svg class="headline-arc" width="409" height="20" viewBox="0 0 409 20" aria-hidden="true"><path d="M5 4 Q204 24 404 4" fill="none" stroke="#f2a33a" stroke-width="3" stroke-linecap="round"/></svg>

  <div class="family-art" role="img" aria-label="医師・看護師と、車いすの祖母を含む三世代家族のイラスト"></div>

  <div class="badge"><span class="date">10/11<small>（水）〜</small></span><span class="note">予約不要</span></div>

  <h1 class="title-band">インフルエンザ予防接種</h1>

  <ul class="points">
    <li><svg width="26" height="22" viewBox="0 0 26 22"><path d="M3 11 L10 18 L23 3" fill="none" stroke="#f2a33a" stroke-width="4" stroke-linecap="round" stroke-linejoin="round"/></svg>インフルエンザに対する抵抗力がつくまで約2週間かかり、<br>その効果は約3〜5ヶ月間持続します。</li>
    <li><svg width="26" height="22" viewBox="0 0 26 22"><path d="M3 11 L10 18 L23 3" fill="none" stroke="#f2a33a" stroke-width="4" stroke-linecap="round" stroke-linejoin="round"/></svg>肺炎球菌ワクチンや他のワクチンとの同時接種は可能です。</li>
    <li><svg width="26" height="22" viewBox="0 0 26 22"><path d="M3 11 L10 18 L23 3" fill="none" stroke="#f2a33a" stroke-width="4" stroke-linecap="round" stroke-linejoin="round"/></svg>体温が37.5度以上、具合が悪い方は別の日に接種しましょう。</li>
    <li><svg width="26" height="22" viewBox="0 0 26 22"><path d="M3 11 L10 18 L23 3" fill="none" stroke="#f2a33a" stroke-width="4" stroke-linecap="round" stroke-linejoin="round"/></svg>妊娠中の方でも予防接種できます。</li>
  </ul>

  <p class="fee-label">接種費用</p>

  <section class="fee-box fee-young">
    <p class="fee-who">13歳から64歳までの方</p>
    <p class="price">4,000円<small>（1回目）</small></p>
    <p class="price second">3,000円<small>（2回目）</small></p>
    <p class="fine">2回目はご希望の方で、1回目接種から<br>4週間後に接種できます。</p>
  </section>

  <section class="fee-box fee-senior">
    <p class="fee-who">65歳以上の方<small>※市町村ごとに異なります</small></p>
    <p class="price">1,500円<small>（接種自己負担）</small></p>
    <p class="period"><span>期間</span>10/10（火）〜 12/31（水）</p>
    <p class="fine">※60歳以上65歳未満で対象の方も同じ費用です。<br>詳しくは受付までお問い合わせください。</p>
  </section>

  <footer class="footer">
    <div class="clinic">
      <p class="dept">内科・消化器内科・糖尿病内科</p>
      <p class="name"><span class="mark"></span>手武内科クリニック</p>
    </div>
    <div class="contact">
      <p>詳細はスタッフにお声掛けください。<br>HPでも公開しています。<br><span class="url">https://temuzeku.com/influenza</span></p>
      <div class="qr-space"></div>
    </div>
  </footer>
</div>
</body>
</html>
```